Postcard for Direct Mailing

I need a Postcard Design that could be used for a direct mailing campaign. I just started a company called BrightLoom (www.brightloom-demo.net) which is an Administrating Consulting Services Company. It is basically a mix of being a Project Manager/Business Analysis/and Virtual Assistant.
My motto is "A Modern Solution to a Classic Problem"

The files that I attached I purchased from stock photos. and I would like them merged together for 1 side that shows how the problem with office staff has been forever.

Also the last one is my logo that should be on the side of the postcard where it can be sent out.

Below I have attached content. I'm not sure if it is too much.

Potential One Side
Are you losing time that could be better spent creating new business leads and focusing on the work at hand?
Worrying about the office work doesn't get it done …..
It may seem like modern technology would streamline your office processes to the point where you can do it all on your own without an assistance, but there is still only so much you can do to strike balance in the midst of running a thriving business.
That’s where BrightLoom Administrative Consulting Services steps in!

Potential Second Side
Let us take that load off your shoulders, while we assist with the taking over tasks that are cutting into your productivity. With the right assistance—or team—fighting on your behalf to create order, I act as another extension of your business and help you with your administrative support needs so that you can concentrate on what really matters – growing your business!
As a part of this customized service, we will take care of the following tasks:
• Word Processing
• Spreadsheet Creation/Tracking
• Research Services
• SlideCraft and other Presentations
• Database Management
• Data Entry
• Internet Research
• Client Relationship Management
• Email Management
• Calendar Management
• Conference Calls
• Vendor Management

Call today for further information, or to arrange a free consultation to determine which services we can provide for you call us at (800) 555-0147 or visit the site www.brightLOOM-demo.net TODAY!

```html
<!DOCTYPE html>
<html lang="en">
<head>
<meta charset="utf-8">
<title>BrightLoom Direct Mail Postcard</title>
<link rel="stylesheet" href="https://fonts.googleapis.com/css2?family=Source+Sans+3:wght@400;600;700&display=swap">
<style>
  :root {
    --page-bg: #1e1e1e;
    --card-white: #ffffff;
    --ink: #2b2b2b;
    --navy: #27306b;
    --blue-deep: #1f3f8f;
    --blue-mid: #3467b8;
    --blue-light: #5b8fd6;
    --band-blue: rgba(38, 66, 140, 0.92);
    --grey-panel-top: #f2f2f2;
    --grey-panel-bottom: #c9cbce;
    --photo-grey-1: #8a8a8a;
    --photo-grey-2: #d6d6d6;
    --photo-office-1: #e9e9e9;
    --photo-office-2: #a8a29a;
    --stamp-line: #9a9a9a;
  }
  * { box-sizing: border-box; margin: 0; padding: 0; }
  html, body {
    width: 1200px; height: 1200px; overflow: hidden;
    background: var(--page-bg);
    font-family: "Source Sans 3", "Myriad Pro", Arial, sans-serif;
  }
  .canvas { position: relative; width: 1200px; height: 1200px; }

  /* ---------- Mailing side ---------- */
  .mail-side {
    position: absolute; left: 419px; top: 26px;
    width: 727px; height: 558px;
    background: var(--card-white);
  }
  .mail-side .intro {
    position: absolute; left: 11px; top: 12px; width: 338px;
    font-size: 15px; line-height: 18.3px; color: var(--ink);
    text-align: justify;
  }
  .service-box {
    position: absolute; left: 0; top: 176px; width: 352px; height: 291px;
    background: radial-gradient(ellipse at 70% 55%, var(--blue-light) 0%, var(--blue-mid) 45%, var(--blue-deep) 100%);
    color: #fff; padding: 10px 11px;
  }
  .service-box .lead {
    font-weight: 700; font-size: 15.5px; line-height: 18.5px; margin-bottom: 6px;
  }
  .service-list { list-style: none; padding-left: 14px; }
  .service-list li {
    font-size: 15px; line-height: 18.4px; position: relative; padding-left: 14px;
  }
  .service-list li::before {
    content: ""; position: absolute; left: 0; top: 8px;
    width: 4px; height: 4px; border-radius: 50%; background: #fff;
  }
  .mail-side .call-out {
    position: absolute; left: 11px; top: 472px; width: 338px;
    font-size: 15px; line-height: 18.3px; color: var(--ink);
  }
  .call-out strong { color: var(--navy); font-weight: 700; }
  .brand-mark {
    display: flex; align-items: center; gap: 8px;
    font-weight: 700; letter-spacing: 0.3px;
  }
  .brand-mark .dot { width: 22px; height: 22px; border-radius: 50%; flex: none; }
  .mail-side .brand-mark {
    position: absolute; left: 372px; top: 54px;
    color: var(--navy); font-size: 28px;
  }
  .mail-side .brand-mark .dot { background: var(--navy); }
  .stamp-box {
    position: absolute; left: 551px; top: 10px; width: 166px; height: 164px;
    border: 1px solid var(--stamp-line);
  }

  /* ---------- Message side ---------- */
  .message-side {
    position: absolute; left: 64px; top: 614px;
    width: 729px; height: 561px;
    background: var(--card-white);
  }
  .photo-classic {
    position: absolute; left: 0; top: 0; width: 521px; height: 198px;
    background: linear-gradient(120deg, var(--photo-grey-1) 0%, var(--photo-grey-2) 50%, #6f6f6f 100%);
  }
  .logo-panel {
    position: absolute; left: 526px; top: 0; width: 203px; height: 197px;
    background: linear-gradient(160deg, var(--blue-mid), var(--blue-deep));
    display: flex; align-items: center; justify-content: center;
  }
  .logo-panel .brand-mark { color: #fff; font-size: 27px; }
  .logo-panel .brand-mark .dot { background: #fff; }
  .headline-band {
    position: absolute; left: 0; top: 205px; width: 521px; height: 138px;
    background: linear-gradient(90deg, var(--blue-deep), var(--band-blue) 70%, #4a74b8);
    padding: 16px 12px 0;
  }
  .headline-band h1 {
    font-weight: 400; color: #fff; font-size: 26.5px; line-height: 35px;
  }
  .photo-modern {
    position: absolute; left: 526px; top: 205px; width: 203px; height: 138px;
    background: linear-gradient(180deg, var(--photo-office-1) 0%, #d2cfca 55%, var(--photo-office-2) 100%);
  }
  .story-panel {
    position: absolute; left: 0; top: 349px; width: 521px; height: 212px;
    background: linear-gradient(180deg, var(--grey-panel-top), var(--grey-panel-bottom));
    padding: 16px 13px; color: var(--ink);
  }
  .story-panel h2 { font-size: 17px; font-weight: 700; margin-bottom: 10px; }
  .story-panel p { font-size: 16.5px; line-height: 22.5px; margin-bottom: 9px; }
  .story-panel p.closing { font-weight: 700; font-size: 17px; line-height: 22.5px; }
  .contact-panel {
    position: absolute; left: 526px; top: 349px; width: 203px; height: 212px;
    background: linear-gradient(180deg, var(--blue-light) 0%, var(--blue-mid) 45%, var(--blue-deep) 100%);
    color: #fff; text-align: right; padding: 0 10px 10px;
    display: flex; flex-direction: column; justify-content: flex-end;
  }
  .contact-panel .web { font-size: 16px; line-height: 20px; }
  .contact-panel .phone { font-size: 28px; line-height: 32px; }
</style>
</head>
<body>
<div class="canvas">

  <section class="mail-side">
    <p class="intro">Let us take that load off your shoulders, while we assist with the taking over tasks that are cutting into your productivity. With the right assistance—or team—fighting on your behalf to create order, I act as another extension of your business and help you with your administrative support needs so that you can concentrate on what really matters – growing your business!</p>

    <div class="service-box">
      <p class="lead">As a part of this customized service, we will take care of the following tasks:</p>
      <ul class="service-list">
        <li>Word Processing</li>
        <li>Spreadsheet Creation/Tracking</li>
        <li>Research Services</li>
        <li>SlideCraft and other Presentations</li>
        <li>Database Management</li>
        <li>Data Entry</li>
        <li>Internet Research</li>
        <li>Client Relationship Management</li>
        <li>Email Management</li>
        <li>Calendar Management</li>
        <li>Conference Calls</li>
        <li>Vendor Management</li>
      </ul>
    </div>

    <p class="call-out">Call today for further information, or to arrange a free consultation to determine which services we can provide for you call us at <strong>(800) 555-0147</strong> or visit the site <strong>www.brightLOOM-demo.net TODAY!</strong></p>

    <div class="brand-mark"><span class="dot"></span>BrightLoom</div>
    <div class="stamp-box"></div>
  </section>

  <section class="message-side">
    <div class="photo-classic" role="img" aria-label="Vintage black-and-white photo of a busy office team crowding around a clerk buried in paperwork"></div>
    <div class="logo-panel">
      <div class="brand-mark"><span class="dot"></span>BrightLoom</div>
    </div>
    <div class="headline-band">
      <h1>Are you losing time that could be better spent creating new business leads and focusing on the work at hand?</h1>
    </div>
    <div class="photo-modern" role="img" aria-label="Modern office photo of stressed colleagues at a meeting table"></div>
    <div class="story-panel">
      <h2>Worrying about the office work doesn't get it done …..</h2>
      <p>It may seem like modern technology would streamline your office processes to the point where you can do it all on your own without an assistance, but there is still only so much you can do to strike balance in the midst of running a thriving business.</p>
      <p class="closing">That’s where BrightLoom Administrative Consulting Services steps in!</p>
    </div>
    <div class="contact-panel">
      <span class="web">www.brightloom-demo.net</span>
      <span class="phone">(800) 555-0147</span>
    </div>
  </section>

</div>
</body>
</html>
```